I need a business card/logo designed that obviously describes my business. We are a residential appraisal and home inspection company in Springfield, MO. We offer residential appraisals, home inspection, pest inspection and radon gas measurement. We have been in business for 18 years and hold state certified residential appraisal licenses and DRUMI certified home inspection licenses. I have a logo that I really like and will attach, but would be open to new suggestions. I like more modern designs than traditional and would like a two sided card with our services, licenses and qualifications on the back.

```html
<!DOCTYPE html>
<html lang="en">
<head>
<meta charset="utf-8">
<title>Larkvale Dwelling Review – Business Card</title>
<link href="https://fonts.googleapis.com/css2?family=Open+Sans:wght@400;600;700&display=swap" rel="stylesheet">
<style>
  :root {
    --backdrop: #8c8c8c;
    --card: #0d0d0d;
    --card-edge: #1a1a1a;
    --orange: #f7941d;
    --tan: #a87b3f;
    --white: #ffffff;
    --soft-white: #e8e8e8;
    --rule: #2b2b2b;
  }
  * { margin: 0; padding: 0; box-sizing: border-box; }
  html, body {
    width: 1200px;
    height: 900px;
    overflow: hidden;
    background: var(--backdrop);
    font-family: "Open Sans", Arial, sans-serif;
  }
  .canvas {
    position: relative;
    width: 1200px;
    height: 900px;
  }
  .card {
    position: absolute;
    left: 250px;
    width: 700px;
    height: 400px;
    background: radial-gradient(ellipse at 50% 35%, var(--card-edge), var(--card) 70%);
    box-shadow: 0 6px 18px rgba(0,0,0,.35);
    overflow: hidden;
  }
  .card--back { top: 40px; }
  .card--front { top: 470px; }

  .wordmark {
    position: absolute;
    display: flex;
    align-items: center;
    gap: 12px;
    font-weight: 700;
    font-size: 30px;
    letter-spacing: .5px;
    white-space: nowrap;
  }
  .wordmark__mark {
    width: 18px;
    height: 18px;
    flex: none;
  }
  .card--back .wordmark {
    left: 50%;
    top: 50%;
    transform: translate(-50%, -50%);
    color: var(--white);
  }
  .card--back .wordmark__mark { background: var(--white); }
  .card--front .wordmark {
    left: 300px;
    top: 100px;
    color: var(--tan);
    font-size: 26px;
  }
  .card--front .wordmark__mark { background: var(--tan); }

  .holder {
    position: absolute;
    left: 50px;
    top: 112px;
  }
  .holder__name {
    color: var(--orange);
    font-weight: 700;
    font-size: 22px;
    line-height: 1.2;
  }
  .holder__role {
    color: var(--soft-white);
    font-size: 15px;
    margin-top: 2px;
  }
  .divider {
    position: absolute;
    left: 300px;
    top: 205px;
    width: 360px;
    height: 1px;
    background: linear-gradient(90deg, transparent, var(--rule) 30%, var(--rule) 70%, transparent);
  }
  .contact {
    position: absolute;
    right: 50px;
    bottom: 48px;
    list-style: none;
    text-align: right;
  }
  .contact__item {
    display: flex;
    justify-content: flex-end;
    align-items: center;
    gap: 12px;
    color: var(--white);
    font-size: 17px;
    line-height: 26px;
  }
  .contact__icon {
    width: 13px;
    height: 13px;
    flex: none;
  }
</style>
</head>
<body>
<main class="canvas">
  <section class="card card--back" aria-label="Card back">
    <div class="wordmark"><span class="wordmark__mark"></span>Larkvale Dwelling Review</div>
  </section>

  <section class="card card--front" aria-label="Card front">
    <div class="holder">
      <p class="holder__name">Marcus Ellery</p>
      <p class="holder__role">Managing Director</p>
    </div>
    <div class="wordmark"><span class="wordmark__mark"></span>Larkvale Dwelling Review</div>
    <div class="divider"></div>
    <ul class="contact">
      <li class="contact__item">123.456.7890
        <svg class="contact__icon" viewBox="0 0 13 13"><rect x="3.5" y="0.8" width="6" height="11.4" rx="1.2" fill="none" stroke="#f7941d" stroke-width="1.4"/><circle cx="6.5" cy="10" r=".8" fill="#f7941d"/></svg>
      </li>
      <li class="contact__item">123.456.7890
        <svg class="contact__icon" viewBox="0 0 13 13"><path d="M1 4.5 Q6.5 0.5 12 4.5 L10.5 6 L8.5 5 L8.5 4 Q6.5 3.2 4.5 4 L4.5 5 L2.5 6 Z" fill="#f7941d"/><rect x="2.5" y="7" width="8" height="5" rx="1" fill="#f7941d"/></svg>
      </li>
      <li class="contact__item">info@youremail.com
        <svg class="contact__icon" viewBox="0 0 13 13"><rect x="0.5" y="2.5" width="12" height="8" fill="#f7941d"/><path d="M0.5 2.5 L6.5 7 L12.5 2.5" fill="none" stroke="#0d0d0d" stroke-width="1"/></svg>
      </li>
      <li class="contact__item">www.website.com
        <svg class="contact__icon" viewBox="0 0 13 13"><rect x="1" y="5" width="6" height="3.6" rx="1.8" transform="rotate(-45 4 6.8)" fill="none" stroke="#f7941d" stroke-width="1.4"/><rect x="6" y="4.4" width="6" height="3.6" rx="1.8" transform="rotate(-45 9 6.2)" fill="none" stroke="#f7941d" stroke-width="1.4"/></svg>
      </li>
    </ul>
  </section>
</main>
</body>
</html>
```